Business Card Design Project

I require a business card with the following information on them for various different people;
name
m:
f:
e:
I have a logo already and will attached that. We are in the construction industry. I require something clean and simple but eye catching at the same time. You can use another colour with our logo if you like and you can style the logo as well if you wish. I am open.
Also it needs to be front and back design.
Industry/Entity Type
Construction
Requirements
Must have
- Logo, name, mobile, fax and email address.
Front and back design

```html
<!DOCTYPE html>
<html lang="en">
<head>
<meta charset="utf-8">
<title>Stonefield Developments – Business Cards</title>
<link rel="stylesheet" href="https://fonts.googleapis.com/css2?family=Arimo:wght@400;700&display=swap">
<style>
  :root {
    --page: #2b2b2b;
    --card: #0c0c0c;
    --card-sheen: #1d1d1d;
    --green: #8ccf3a;
    --green-deep: #2f6a1a;
    --silver: #9a9a9a;
    --silver-light: #f2f2f2;
    --text: #f2f2f2;
  }
  * { box-sizing: border-box; margin: 0; padding: 0; }
  html, body { width: 1200px; height: 900px; overflow: hidden; }
  body {
    background: var(--page);
    font-family: "Arimo", Arial, sans-serif;
    position: relative;
  }
  .card {
    position: absolute;
    width: 640px;
    height: 366px;
    background: linear-gradient(160deg, var(--card-sheen) 0%, var(--card) 45%, var(--card) 100%);
    overflow: hidden;
    box-shadow: 0 10px 30px rgba(0,0,0,.5);
  }
  .card--front { left: 60px; top: 50px; }
  .card--back { left: 500px; top: 480px; }

  .card__bands { position: absolute; inset: 0; width: 100%; height: 100%; }

  .brand {
    position: absolute;
    left: 0; right: 0;
    text-align: center;
    color: var(--green);
    font-weight: 400;
    font-size: 34px;
    letter-spacing: 1px;
  }
  .card--front .brand { top: 62px; }
  .card--back .brand { top: 120px; }

  .contact {
    position: absolute;
    left: 40px;
    top: 145px;
    color: var(--text);
  }
  .contact__name {
    color: var(--green);
    font-size: 27px;
    font-weight: 400;
    margin-bottom: 10px;
  }
  .contact__grid {
    display: grid;
    grid-template-columns: 190px auto;
    row-gap: 8px;
    font-size: 16px;
  }
  .contact__item { display: flex; align-items: center; gap: 10px; }
  .contact__icon { width: 16px; height: 16px; flex: none; }
</style>
</head>
<body>

<section class="card card--front" aria-label="Business card front">
  <svg class="card__bands" viewBox="0 0 640 366" preserveAspectRatio="none" aria-hidden="true">
    <defs>
      <linearGradient id="silverBar" x1="0" x2="1">
        <stop offset="0" stop-color="#444"/>
        <stop offset="0.6" stop-color="#bbb"/>
        <stop offset="1" stop-color="#eee"/>
      </linearGradient>
    </defs>
    <polygon points="420,270 640,236 640,246 420,276" fill="url(#silverBar)"/>
    <polygon points="0,318 640,250 640,262 0,332" fill="#8ccf3a"/>
    <polygon points="0,332 640,262 640,366 0,366" fill="#0a0a0a"/>
    <polygon points="0,334 250,306 262,314 0,348" fill="#2f6a1a"/>
  </svg>

  <div class="brand">Stonefield Developments</div>

  <div class="contact">
    <h1 class="contact__name">Mark Henley</h1>
    <div class="contact__grid">
      <div class="contact__item">
        <svg class="contact__icon" viewBox="0 0 16 16" aria-hidden="true"><path d="M3 1l3 3-2 2c1 2 3 4 5 5l2-2 3 3-2 3C7 14 2 9 1 3z" fill="var(--green)"/></svg>
        <span>03 9000 4815</span>
      </div>
      <div class="contact__item">
        <svg class="contact__icon" viewBox="0 0 16 16" aria-hidden="true"><rect x="4" y="1" width="8" height="14" rx="2" fill="none" stroke="var(--green)" stroke-width="2"/></svg>
        <span>0400 555 219</span>
      </div>
      <div class="contact__item">
        <svg class="contact__icon" viewBox="0 0 16 16" aria-hidden="true"><rect x="1" y="6" width="14" height="8" rx="1" fill="var(--green)"/><rect x="4" y="2" width="8" height="5" fill="none" stroke="var(--green)" stroke-width="1.5"/></svg>
        <span>03 9000 4816</span>
      </div>
      <div class="contact__item">
        <svg class="contact__icon" viewBox="0 0 16 16" aria-hidden="true"><rect x="1" y="3" width="14" height="10" fill="none" stroke="var(--green)" stroke-width="1.5"/><path d="M1 3l7 6 7-6" fill="none" stroke="var(--green)" stroke-width="1.5"/></svg>
        <span>mark@stonefieldbuild.com.au</span>
      </div>
    </div>
  </div>
</section>

<section class="card card--back" aria-label="Business card back">
  <svg class="card__bands" viewBox="0 0 640 366" preserveAspectRatio="none" aria-hidden="true">
    <defs>
      <linearGradient id="chromeBar" x1="0" x2="1" y1="0" y2="0.2">
        <stop offset="0" stop-color="#111"/>
        <stop offset="0.45" stop-color="#888"/>
        <stop offset="0.7" stop-color="#f5f5f5"/>
        <stop offset="1" stop-color="#555"/>
      </linearGradient>
    </defs>
    <polygon points="0,300 640,230 640,234 0,304" fill="#8ccf3a"/>
    <polygon points="0,312 640,242 640,300 0,366" fill="url(#chromeBar)"/>
  </svg>

  <div class="brand">Stonefield Developments</div>
</section>

</body>
</html>
```